Business Card Design Project

Design is for the business card of a holistic, integral therapist. Design is required for front (colour / pattern) and back (white, with text as below).

Please prepare the design using placeholder text. I will work with the winning submission to complete the final information in the last iteration.

To give you a sense of her services a profile is below:
- I offer an integrative approach for effective relief of many issues such as anxiety, panic attacks, relationship difficulties, and health problems. In my counselling sessions I mainly use QBR {Quiet Balance Release } which taps into the body's energy system (meridians) to clear up blockages and limiting /distorted thinking and beliefs. I also work on expanding awareness as well as enhancing relationships.Clients have found the sessions life changing and report feeling lighter, clearer more empowered and connected to themselves and others.

Target Market(s)

Well educated, upper socioeconomic people seeking purpose and happiness in their lives.

Industry/Entity Type

Health

Requirements
Must have
• Must have the following text on front

First Name, Last Name
LLB, ND, Dip C
Counselling & Naturopathy
Quiet Balnce Release and Marlow Therapy

Adress 1 Line 1
Adress 1 Line 2

Adress 2 Line 1
Adress 2 Line 2

xxx.xxx@xxxxx.com

Tel: 0XXX XXX XXX

Must have the following text on reverse - which should be primarily white.

Next appointment
Date:
Time:
Nice to have
• Example colour palettes

http://www.huebinder.example/swatch/512093/velvet_lantern
http://www.huebinder.example/swatch/318420/Quiet_Orchard
http://www.huebinder.example/swatch/607215/Morning_Over_Tides

Example images that may be useful...
http://www.shopvarn.example/gp/product/images/4719205536/ref=dp_image_text_0?ie=UTF8&n=517302&s=books
http://www.shopvarn.example/gp/customer-media/product-gallery/6284019573/ref=cm_ciu_pdp_images_all
http://en.loreweb.example/wiki/File:Lotus_Grid_256bw.gif

```html
<!DOCTYPE html>
<html lang="en">
<head>
<meta charset="utf-8">
<title>Counselling &amp; Naturopathy – Business Card</title>
<link rel="stylesheet" href="https://fonts.googleapis.com/css2?family=Oswald:wght@300;400;600;700&display=swap">
<style>
  :root {
    --backdrop: #a9a9a9;
    --backdrop-light: #cfcfcf;
    --card-yellow: #ecd37c;
    --stripe-red: #df5038;
    --stripe-faint: rgba(223,80,56,0.14);
    --panel-red: #bf2541;
    --gold-light: #fbe7a6;
    --gold: #e6bd5c;
    --gold-dark: #b0802c;
    --white: #ffffff;
    --off-white: #fbf8f1;
  }
  * { margin: 0; padding: 0; box-sizing: border-box; }
  html, body { width: 1200px; height: 1200px; overflow: hidden; }
  body {
    position: relative;
    background: radial-gradient(ellipse at center, var(--backdrop-light) 0%, var(--backdrop) 75%);
    font-family: "Oswald", "Arial Narrow", sans-serif;
  }
  .card {
    position: absolute;
    left: 187px;
    width: 859px;
    height: 493px;
    box-shadow: 18px 22px 30px rgba(0,0,0,0.55);
    overflow: hidden;
  }
  .card--front {
    top: 79px;
    background:
      repeating-linear-gradient(135deg,
        var(--card-yellow) 0 30px,
        var(--stripe-red) 30px 37px,
        var(--card-yellow) 37px 42px);
  }
  .card--back {
    top: 631px;
    background:
      repeating-linear-gradient(135deg,
        var(--white) 0 30px,
        var(--stripe-faint) 30px 37px,
        var(--white) 37px 42px);
  }

  .ornament-frame {
    position: absolute;
    left: 8px; top: 24px;
    width: 843px; height: 450px;
    border-radius: 50% / 32%;
    background: radial-gradient(ellipse at center, rgba(255,246,214,0.9) 0%, rgba(245,222,150,0.6) 55%, rgba(236,211,124,0) 80%);
  }

  .panel {
    position: absolute;
    left: 123px;
    width: 614px;
    height: 304px;
    box-shadow: 10px 14px 22px rgba(0,0,0,0.45);
  }
  .card--front .panel { top: 89px; background: var(--panel-red); }
  .card--back .panel {
    top: 87px;
    background: var(--off-white);
    box-shadow: 6px 10px 20px rgba(0,0,0,0.25);
    border: 1px solid rgba(191,37,65,0.25);
  }

  .gold-text {
    background: linear-gradient(180deg, var(--gold-light) 0%, var(--gold) 50%, var(--gold-dark) 100%);
    -webkit-background-clip: text;
    background-clip: text;
    color: transparent;
    text-transform: uppercase;
    filter: drop-shadow(1px 2px 1px rgba(60,0,10,0.55));
  }
  .centered { position: absolute; left: 0; width: 100%; text-align: center; white-space: nowrap; line-height: 1; }

  .name { top: 32px; font-size: 40px; letter-spacing: 6px; font-weight: 700; }
  .name .last { font-weight: 300; letter-spacing: 3px; font-size: 36px; }
  .credentials { top: 75px; font-size: 19px; letter-spacing: 3px; font-weight: 600; }
  .practice { top: 105px; font-size: 27px; letter-spacing: 4px; font-weight: 600; }
  .modalities { top: 138px; font-size: 15px; letter-spacing: 2.5px; font-weight: 600; }

  .address {
    position: absolute;
    left: 61px; top: 168px;
    font-size: 16px;
    font-style: normal;
    line-height: 23px;
    letter-spacing: 2px;
    font-weight: 600;
  }
  .contact {
    position: absolute;
    top: 276px;
    font-size: 11px;
    line-height: 1;
    letter-spacing: 1.5px;
    font-weight: 400;
  }
  .contact--email { left: 80px; }
  .contact--tel { left: 406px; text-transform: none; }

  .red-text {
    color: var(--panel-red);
    text-transform: uppercase;
    font-weight: 600;
    line-height: 1;
  }
  .appointment-title { top: 47px; font-size: 27px; letter-spacing: 5px; }
  .field-label { position: absolute; left: 42px; font-size: 28px; letter-spacing: 4px; }
  .field-label--date { top: 124px; }
  .field-label--time { top: 199px; }
  .write-line {
    position: absolute;
    left: 33px; top: 173px;
    width: 571px; height: 4px;
    background: linear-gradient(90deg, rgba(230,170,110,0.4) 0%, var(--gold) 25%, var(--gold-dark) 70%, var(--gold) 100%);
  }
</style>
</head>
<body>
  <section class="card card--front" aria-label="Business card front">
    <div class="ornament-frame" role="img" aria-label="Gold key-fret border framing a pale lotus grid mandala"></div>
    <div class="panel">
      <h1 class="centered name gold-text">First Name, <span class="last">Last Name</span></h1>
      <p class="centered credentials gold-text">LLB, ND, Dip C</p>
      <p class="centered practice gold-text">Counselling &amp; Naturopathy</p>
      <p class="centered modalities gold-text">Quiet Balnce Release and Marlow Therapy</p>
      <address class="address gold-text">
        Adress 1 Line 1<br>
        Adress 1 Line 2<br>
        Adress 2 Line 1<br>
        Adress 2 Line 2
      </address>
      <p class="contact contact--email gold-text">xxx.xxx@xxxxx.com</p>
      <p class="contact contact--tel gold-text">Tel: 0XXX XXX XXX</p>
    </div>
  </section>

  <section class="card card--back" aria-label="Business card back">
    <div class="panel">
      <h2 class="centered appointment-title red-text">Next Appointment</h2>
      <p class="field-label field-label--date red-text">Date:</p>
      <div class="write-line"></div>
      <p class="field-label field-label--time red-text">Time:</p>
    </div>
  </section>
</body>
</html>
```